Design WORDPRESS Website for E Commerce Business

We are needing a WORDPRESS website for an E Commerce Business that is supplying quailty kids / baby products.

Target Market(s)

Female / Working Mums / New Mums

Industry/Entity Type

Business

Number of Pages Required

1 page

Font styles to use
Sans Serif

Colors
33b8a4
f8fcfd
d3a5cc
f7f1f7
cbcbcb
9d9d9d

```html
<!DOCTYPE html>
<html lang="en">
<head>
<meta charset="utf-8">
<title>Cub &amp; Nest — Baby Store</title>
<link rel="stylesheet" href="https://fonts.googleapis.com/css2?family=Roboto:ital,wght@0,400;0,500;0,700;0,900;1,700&family=Fredoka:wght@600&family=Pacifico&display=swap">
<style>
:root{
  --teal:#33b8a4;
  --teal-dark:#259c8a;
  --teal-deep:#1f8f7d;
  --paper:#f8fcfd;
  --pink:#d3a5cc;
  --pink-soft:#f7f1f7;
  --line:#cbcbcb;
  --grey:#9d9d9d;
  --ink:#222;
  --text:#555;
  --dark:#222222;
  --star:#f3b420;
}
*{box-sizing:border-box;margin:0;padding:0}
html,body{width:1200px;height:3349px;overflow:hidden}
body{background:#fff;font-family:'Roboto',sans-serif;color:var(--text);position:relative}
.abs{position:absolute}
a{color:inherit;text-decoration:none}

/* top bar */
.topbar{left:0;top:0;width:1200px;height:38px;background:var(--teal);color:#fff;font-size:12px}
.topbar .left{left:80px;top:11px;display:flex;gap:26px}
.topbar .right{right:80px;top:11px;display:flex;gap:26px}
.topbar .item{display:flex;align-items:center;gap:6px}

/* header */
.logo{left:80px;top:56px;display:flex;align-items:center;gap:10px}
.logo .mark{width:40px;height:40px;border-radius:50%;background:var(--grey)}
.logo .name{font-weight:700;font-size:30px;color:var(--teal);line-height:1}
.search{left:389px;top:75px;width:473px;height:32px;border:1px solid var(--line);border-radius:16px;display:flex;align-items:center;font-size:11px;color:#666}
.search .cat{width:160px;padding-left:18px;border-right:1px solid var(--line);height:100%;display:flex;align-items:center;justify-content:space-between;padding-right:12px}
.search .q{flex:1;padding-left:14px}
.search .go{width:28px;height:28px;border-radius:50%;background:var(--teal);margin-right:2px;display:flex;align-items:center;justify-content:center}
.pill{top:76px;height:28px;border-radius:14px;background:var(--teal);color:#fff;display:flex;align-items:center;gap:12px;padding:0 12px;font-size:12px;font-weight:700}
.nav{left:80px;top:137px;width:1040px;height:34px;border-top:1px solid #e4e4e4;border-bottom:1px solid #e4e4e4;display:flex;justify-content:space-between;align-items:center;padding:0 57px;font-size:12px;font-weight:500;color:var(--ink);letter-spacing:.2px}

/* hero */
.hero-main{left:80px;top:194px;width:773px;height:336px;background:linear-gradient(90deg,#dff4ee 0%,#c9ece6 50%,#e6f5f2 100%);overflow:hidden}
.hero-art{left:480px;top:20px;width:280px;height:300px;background:radial-gradient(circle at 50% 45%,#f6cf9c 0 30%,#7fcfc3 45%,transparent 70%)}
.hero-title{left:26px;top:55px;font-family:'Fredoka',sans-serif;font-weight:600;color:var(--teal);line-height:1.1}
.hero-title .l1{font-size:36px}
.hero-title .l2{font-size:32px;color:#8cc3b8;font-style:italic}
.hero-copy{left:26px;top:142px;width:270px;font-size:12px;line-height:1.55;color:#333}
.btn{display:inline-flex;align-items:center;gap:8px;background:var(--teal);color:#fff;font-weight:700;font-size:12px;border-radius:20px}
.hero-btn{left:26px;top:198px;height:38px;padding:0 24px}
.hero-dots{left:30px;top:305px;display:flex;gap:8px}
.dot{width:12px;height:12px;border-radius:50%;background:#b8b8b8;border:2px solid #e8e8e8}
.dot.on{background:var(--teal-dark)}
.side{left:880px;width:240px;height:156px;overflow:hidden}
.side-boys{top:194px;background:linear-gradient(90deg,#5fd0bd,#36b8a4)}
.side-girls{top:375px;background:linear-gradient(90deg,#f1f1f1,#d9d9d9)}
.side .art{top:10px;width:110px;height:140px;border-radius:50% 50% 0 0}
.side-boys .art{left:120px;background:linear-gradient(#8fdacc,#2d77a8)}
.side-girls .art{left:8px;background:linear-gradient(#e8e0d8,#c4b8b8)}
.side .t{font-family:'Fredoka',sans-serif;font-weight:600;line-height:.95}
.side .t1{font-size:34px;color:rgba(255,255,255,.55)}
.side .t2{font-size:17px;font-style:italic;color:#fff}
.side-boys .txt{left:18px;top:30px}
.side-girls .txt{left:118px;top:30px;text-align:right}
.side-girls .t1{color:rgba(150,150,150,.6)}
.side .more{font-size:11px;font-weight:700;margin-top:18px;color:#222}

/* section heads */
.head{left:0;width:1200px;text-align:center}
.head h2{font-size:24px;font-weight:700;color:var(--ink);letter-spacing:.2px}
.head .rule{display:block;width:70px;height:2px;background:var(--teal);margin:16px auto 0}

/* product cards */
.card{width:240px;height:418px;border:1px solid #e3e3e3;background:#fff;text-align:center}
.card .pic{position:absolute;left:22px;top:20px;width:194px;height:190px;border-radius:4px}
.card h3{position:absolute;left:0;right:0;top:252px;font-size:16px;font-weight:700;color:var(--ink)}
.card .stars{position:absolute;left:0;right:0;top:280px;font-size:9px;color:var(--star);letter-spacing:1px}
.card .price{position:absolute;left:0;right:0;top:298px;font-size:26px;font-weight:700;font-style:italic;color:#8a8a8a}
.card .btn{position:absolute;left:48px;top:352px;width:144px;height:26px;border-radius:13px;justify-content:center;font-size:10px;gap:6px}
.row-dots{left:0;width:1200px;display:flex;justify-content:center;gap:6px}
.row-dots .dot{width:11px;height:11px;border:0}

/* promo band */
.promo{left:0;top:1175px;width:1200px;height:233px;background:var(--teal);overflow:hidden}
.promo .kid1{left:112px;top:40px;width:120px;height:160px;border-radius:50% 50% 40% 40%;background:linear-gradient(#f3d2b4,#e6bd97)}
.promo .kid2{left:960px;top:10px;width:140px;height:223px;border-radius:40% 40% 0 0;background:linear-gradient(#6d6a78,#2c3a6b 55%,#b8743a 62%,#2c3a6b 75%)}
.promo .script{left:0;width:1200px;top:52px;text-align:center;font-family:'Pacifico',cursive;font-size:20px;color:#12423b}
.promo .big{left:0;width:1200px;top:86px;text-align:center;font-size:44px;font-weight:700;color:#fff;letter-spacing:.5px}
.promo .btn{left:544px;top:154px;height:28px;padding:0 22px;background:#17695d;font-size:11px;border-radius:14px}

/* testimonial */
.quote{left:0;top:2053px;width:1200px;height:354px;background:#a0a0a0}
.quote .mark{left:0;width:1200px;top:44px;text-align:center;font-size:64px;font-weight:900;color:#6e6e6e;line-height:1}
.quote p{position:absolute;left:270px;width:660px;top:98px;text-align:center;font-size:16px;line-height:1.5;color:#fff}
.quote .avatar{left:570px;top:200px;width:60px;height:60px;border-radius:50%;border:3px solid #ddd;background:linear-gradient(#7a6a60,#3a2e28)}
.quote .who{left:0;width:1200px;top:272px;text-align:center;font-size:12px;font-weight:700;color:#222}
.quote .role{left:0;width:1200px;top:292px;text-align:center;font-size:12px;color:#eee}
.arrow-sq{width:34px;height:34px;background:#fff;border-radius:3px;display:flex;align-items:center;justify-content:center}

/* brands */
.brands{left:101px;top:2553px;display:flex;gap:18px}
.brand{width:128px;height:92px;border:1px solid #e3e3e3;background:#fff;display:flex;align-items:center;justify-content:center}
.brand span{display:block;width:74px;height:30px;border-radius:15px}
.circ-arrow{width:26px;height:26px;border-radius:50%;background:#ddd;display:flex;align-items:center;justify-content:center}

/* newsletter */
.news{left:0;top:2700px;width:1200px;height:107px;background:var(--teal)}
.news h2{position:absolute;left:80px;top:30px;font-family:'Pacifico',cursive;font-weight:400;font-size:34px;color:#fff;line-height:1.2}
.news .field{left:347px;top:38px;width:420px;height:38px;background:var(--teal-deep);display:flex;align-items:center;justify-content:space-between;padding:0 14px;font-size:12px;color:#fff}
.news .sep{left:790px;top:22px;width:1px;height:66px;background:rgba(255,255,255,.45)}
.news .phone{left:815px;top:40px;display:flex;align-items:center;gap:18px;font-size:24px;font-weight:700;color:#fff;font-style:italic}

/* footer */
.footer{left:0;top:2807px;width:1200px;height:370px;background:var(--dark)}
.fcol{top:70px;width:170px}
.fcol h4{font-size:12px;font-weight:700;color:#fff;margin-bottom:14px;letter-spacing:.3px}
.fcol li{list-style:none;font-size:11px;color:#cfcfcf;line-height:21.5px}
.bottom-links{left:0;width:1200px;top:3206px;display:flex;justify-content:center;gap:28px;font-size:11px;color:#555;letter-spacing:.3px}
.bottom-links .b{color:#999}
.copy{left:0;width:1200px;top:3244px;text-align:center;font-size:11px;color:#999}
.social{left:0;width:1200px;top:3284px;display:flex;justify-content:center;gap:14px}
.social span{width:28px;height:28px;border-radius:50%;background:var(--teal)}
</style>
</head>
<body>

<div class="abs topbar">
  <div class="abs left">
    <span class="item"><svg width="12" height="12" viewBox="0 0 24 24"><path fill="#fff" d="M6.6 10.8a15 15 0 0 0 6.6 6.6l2.2-2.2c.3-.3.7-.4 1-.2 1.1.4 2.3.6 3.6.6.6 0 1 .4 1 1V20c0 .6-.4 1-1 1A17 17 0 0 1 3 4c0-.6.4-1 1-1h3.5c.6 0 1 .4 1 1 0 1.3.2 2.5.6 3.6.1.3 0 .7-.2 1z"/></svg>+555-010-4821</span>
    <span class="item"><svg width="13" height="10" viewBox="0 0 26 20"><rect x="1" y="1" width="24" height="18" rx="2" fill="none" stroke="#fff" stroke-width="2"/><path d="M2 2l11 9 11-9" fill="none" stroke="#fff" stroke-width="2"/></svg>hello@cubnest.co</span>
  </div>
  <div class="abs right">
    <span class="item"><svg width="12" height="12" viewBox="0 0 24 24"><circle cx="12" cy="12" r="10" fill="none" stroke="#fff" stroke-width="2.4"/><path d="M12 6v6l4 3" stroke="#fff" stroke-width="2.4" fill="none"/></svg>Mon - Fri: 6.00 AM - 4.00 PM</span>
    <span class="item"><svg width="12" height="12" viewBox="0 0 24 24"><circle cx="12" cy="7" r="5" fill="#fff"/><path d="M2 23c0-6 4.5-9 10-9s10 3 10 9z" fill="#fff"/></svg>Login / Sign Up</span>
  </div>
</div>

<div class="abs logo"><span class="mark"></span><span class="name">Cub &amp; Nest</span></div>
<div class="abs search">
  <div class="cat">Search in Categories <svg width="8" height="6" viewBox="0 0 8 6"><path d="M0 0h8L4 6z" fill="#777"/></svg></div>
  <div class="q">Search for a Category, Brand or Product</div>
  <div class="go"><svg width="12" height="12" viewBox="0 0 24 24"><circle cx="10" cy="10" r="7" fill="none" stroke="#fff" stroke-width="3"/><path d="M15 15l6 6" stroke="#fff" stroke-width="3"/></svg></div>
</div>
<div class="abs pill" style="left:972px"><svg width="14" height="14" viewBox="0 0 24 24"><path d="M4 9h16l-1.5 12h-13z" fill="#fff"/><path d="M8 9V6a4 4 0 0 1 8 0v3" stroke="#fff" stroke-width="2" fill="none"/></svg><span>0</span></div>
<div class="abs pill" style="left:1060px"><svg width="14" height="14" viewBox="0 0 24 24"><path d="M12 21l-8.5-8.5A5 5 0 0 1 12 5a5 5 0 0 1 8.5 7.5z" fill="#fff"/></svg><span>0</span></div>

<nav class="abs nav">
  <a>HOME</a><a>ABOUT US</a><a>KIDS CLOTHES</a><a>TOY &amp; BOOKS</a><a>STROLLERS</a><a>FEEDING</a><a>BABY SHOWER</a><a>SHOP</a><a>GIFTS</a><a>CONTACT US</a>
</nav>

<div class="abs hero-main">
  <div class="abs hero-art" role="img" aria-label="Illustrated baby sitting with colourful toy truck and blocks"></div>
  <div class="abs hero-title"><div class="l1">UP TO 60% OFF</div><div class="l2">NEW COLLECTION SUMMER</div></div>
  <p class="abs hero-copy">Lorem ipsum dolor sit amet, consectetur adipiscing elit. Aenean varius turpis nibh, non hendrerit metus interdum eget.</p>
  <a class="abs btn hero-btn">SHOP NOW <span>›</span></a>
  <div class="abs hero-dots"><span class="dot on"></span><span class="dot"></span><span class="dot"></span></div>
</div>
<div class="abs side side-boys">
  <div class="abs art" role="img" aria-label="Photo of a smiling boy in a striped shirt"></div>
  <div class="abs txt"><div class="t t1">SHOP</div><div class="t t2">FOR BOYS</div><div class="more">CLICK HERE ›</div></div>
</div>
<div class="abs side side-girls">
  <div class="abs art" role="img" aria-label="Photo of a girl wearing glasses"></div>
  <div class="abs txt"><div class="t t1">SHOP</div><div class="t t2">FOR GIRLS</div><div class="more">CLICK HERE ›</div></div>
</div>

<div class="abs head" style="top:588px"><h2>MOST POPULAR</h2><span class="rule"></span></div>

<div class="abs card" style="left:80px;top:693px"><div class="pic" role="img" aria-label="Yellow wooden giraffe toy" style="background:radial-gradient(circle,#f5c51c 0 35%,#fff 60%)"></div><h3>Suspendisse Tellus</h3><div class="stars">★★★★☆</div><div class="price">$54.00</div><a class="btn">ADD TO CART</a></div>
<div class="abs card" style="left:347px;top:693px"><div class="pic" role="img" aria-label="Baby sitting with a toy car" style="background:radial-gradient(circle,#e9c7a5 0 30%,#a9c4dc 45%,#fff 65%)"></div><h3>Vestibulum</h3><div class="stars">★★★★☆</div><div class="price">$20.00</div><a class="btn">ADD TO CART</a></div>
<div class="abs card" style="left:615px;top:693px"><div class="pic" role="img" aria-label="Stack of folded blue baby clothes" style="background:radial-gradient(circle,#a8c8ec 0 35%,#fff 62%)"></div><h3>Mauris Faucibus</h3><div class="stars">★★★★☆</div><div class="price">$99.00</div><a class="btn">ADD TO CART</a></div>
<div class="abs card" style="left:882px;top:693px"><div class="pic" role="img" aria-label="Baby bath bottles, towel and rubber duck" style="background:radial-gradient(circle,#b9e07a 0 25%,#8fd0e0 45%,#fff 65%)"></div><h3>Duis Fermentum</h3><div class="stars">★★★★☆</div><div class="price">$12.00</div><a class="btn">ADD TO CART</a></div>
<div class="abs row-dots" style="top:1138px"><span class="dot on"></span><span class="dot"></span><span class="dot"></span></div>

<section class="abs promo">
  <div class="abs kid1" role="img" aria-label="Photo of a sitting baby"></div>
  <div class="abs kid2" role="img" aria-label="Photo of a boy in a cap holding a ball"></div>
  <div class="abs script">Baby Store Baby Shopping</div>
  <div class="abs big">20% OFF FOR ALL PRODUCTS</div>
  <a class="abs btn">CLICK HERE</a>
</section>

<div class="abs head" style="top:1466px"><h2>FEATURED PRODUCTS</h2><span class="rule"></span></div>

<div class="abs card" style="left:80px;top:1570px"><div class="pic" role="img" aria-label="Baby in red shirt with stacking rings" style="background:radial-gradient(circle,#e9c7a5 0 25%,#e64a3c 40%,#fff 65%)"></div><h3>Vivamus</h3><div class="stars">★★★★☆</div><div class="price">$54.00</div><a class="btn">ADD TO CART</a></div>
<div class="abs card" style="left:347px;top:1570px"><div class="pic" role="img" aria-label="Yellow rubber duck" style="background:radial-gradient(circle,#f7d21a 0 35%,#fff 60%)"></div><h3>Ut Interdum</h3><div class="stars">★★★★☆</div><div class="price">$20.00</div><a class="btn">ADD TO CART</a></div>
<div class="abs card" style="left:615px;top:1570px"><div class="pic" role="img" aria-label="Baby crawling with toy blocks" style="background:radial-gradient(circle,#e9c7a5 0 25%,#7aa4d6 42%,#fff 65%)"></div><h3>Curabitur Libero</h3><div class="stars">★★★★☆</div><div class="price">$99.00</div><a class="btn">ADD TO CART</a></div>
<div class="abs card" style="left:882px;top:1570px"><div class="pic" role="img" aria-label="Plush blue dragon toy" style="background:radial-gradient(circle,#5ac7d8 0 35%,#fff 62%)"></div><h3>Nam Congue</h3><div class="stars">★★★★☆</div><div class="price">$12.00</div><a class="btn">ADD TO CART</a></div>
<div class="abs row-dots" style="top:2018px"><span class="dot on"></span><span class="dot"></span><span class="dot"></span></div>

<section class="abs quote">
  <div class="abs mark">“</div>
  <p>Fusce elementum ac leo in sollicitudin. Aliquam a velit velit. Pellentesque et semper libero. Praesent non efficitur libero. Integer sit amet ipsum ut arcu placerat feugiat in ac quam. Mauris eu arcu eget ante rhoncus pulvinar ut et justo.</p>
  <div class="abs avatar" role="img" aria-label="Customer portrait"></div>
  <div class="abs who">- SODALES</div>
  <div class="abs role">Curabitus Libero Item</div>
  <div class="abs arrow-sq" style="left:92px;top:157px"><svg width="10" height="12" viewBox="0 0 10 12"><path d="M8 1L2 6l6 5" fill="none" stroke="#333" stroke-width="2"/></svg></div>
  <div class="abs arrow-sq" style="left:1072px;top:157px"><svg width="10" height="12" viewBox="0 0 10 12"><path d="M2 1l6 5-6 5" fill="none" stroke="#333" stroke-width="2"/></svg></div>
</section>

<div class="abs head" style="top:2463px"><h2>TOP BRANDS</h2><span class="rule"></span></div>
<div class="abs circ-arrow" style="left:54px;top:2586px"><svg width="8" height="10" viewBox="0 0 8 10"><path d="M6 1L2 5l4 4" fill="none" stroke="#666" stroke-width="2"/></svg></div>
<div class="abs brands">
  <div class="brand"><span style="background:#cfe3f3"></span></div>
  <div class="brand"><span style="background:#dce9f6"></span></div>
  <div class="brand"><span style="background:#cfdcf0"></span></div>
  <div class="brand"><span style="background:#f2d6cf"></span></div>
  <div class="brand"><span style="background:#d6e0f2"></span></div>
  <div class="brand"><span style="background:#f5d7e6"></span></div>
  <div class="brand"><span style="background:#dce9f6"></span></div>
</div>
<div class="abs circ-arrow" style="left:1118px;top:2586px"><svg width="8" height="10" viewBox="0 0 8 10"><path d="M2 1l4 4-4 4" fill="none" stroke="#666" stroke-width="2"/></svg></div>

<section class="abs news">
  <h2>Newsletter</h2>
  <div class="abs field"><span>Enter your email here</span><svg width="16" height="16" viewBox="0 0 24 24"><path d="M2 12L22 3l-6 18-4-7z" fill="#fff"/></svg></div>
  <div class="abs sep"></div>
  <div class="abs phone"><svg width="22" height="22" viewBox="0 0 24 24"><path fill="#fff" d="M6.6 10.8a15 15 0 0 0 6.6 6.6l2.2-2.2c.3-.3.7-.4 1-.2 1.1.4 2.3.6 3.6.6.6 0 1 .4 1 1V20c0 .6-.4 1-1 1A17 17 0 0 1 3 4c0-.6.4-1 1-1h3.5c.6 0 1 .4 1 1 0 1.3.2 2.5.6 3.6.1.3 0 .7-.2 1z"/></svg>+ (555) 010 482 1193</div>
</section>

<footer class="abs footer">
  <div class="abs fcol" style="left:80px"><h4>BOYS' CLOTHING</h4><ul><li>T-Shirts</li><li>Shirts</li><li>Shorts</li><li>Jeans</li><li>Pants</li><li>Sportswear</li><li>Sweaters</li><li>Coats &amp; Jackets</li></ul></div>
  <div class="abs fcol" style="left:258px"><h4>GIRLS' CLOTHING</h4><ul><li>Dresses</li><li>Skirts</li><li>T-Shirts</li><li>Shirts &amp; Blouse</li><li>Shorts</li><li>Jeans</li><li>Pants</li><li>Sweaters</li><li>Coats &amp; Jackets</li></ul></div>
  <div class="abs fcol" style="left:434px"><h4>TOYS</h4><ul><li>Boys' Toys</li><li>Girls' Toys</li><li>Infant and Preschool</li><li>Educational</li></ul></div>
  <div class="abs fcol" style="left:613px"><h4>BABY</h4><ul><li>Travel</li><li>Car Seats</li><li>Activity</li><li>Bath &amp; Potty</li><li>Strollers</li><li>Travel Systems</li><li>Buggies</li><li>Travel Cots</li></ul></div>
  <div class="abs fcol" style="left:791px"><h4>ABOUT</h4><ul><li>About us</li><li>Write to us</li><li>Careers</li><li>Take a Tour</li></ul></div>
  <div class="abs fcol" style="left:969px"><h4>HELP</h4><ul><li>Help</li><li>Contact us</li><li>Shipping</li><li>Returns Process</li><li>Returns Policy</li><li>FAQs</li></ul></div>
</footer>

<div class="abs bottom-links"><a>MY ACCOUNT</a><span class="b">•</span><a>SHIPPING &amp; RETURNS</a><span class="b">•</span><a>PRIVACY POLICY</a><span class="b">•</span><a>TERMS &amp; CONDITIONS</a></div>
<div class="abs copy">Cub &amp; Nest © 2017 / All Rights Reserved</div>
<div class="abs social"><span></span><span></span><span></span><span></span><span></span><span></span></div>

</body>
</html>
```